- Redesign our business card
- Logo remains unchanged
- Current business card attached

Target Market(s)

We are a property management company

Industry/Entity Type

Business

```html
<!DOCTYPE html>
<html lang="en">
<head>
<meta charset="utf-8">
<title>Hartwell Property Group – Business Card</title>
<link rel="stylesheet" href="https://fonts.googleapis.com/css2?family=Cinzel:wght@400;500&family=Cormorant+Garamond:wght@400;500;600&display=swap">
<style>
  :root {
    --page: #e9e6e1;
    --card-black: #0c0c0c;
    --card-charcoal: #2a2a2a;
    --white: #ffffff;
    --paper: #f4f4f4;
    --cream: #e6d7ab;
    --olive: #8a8a55;
    --slate: #7a7b80;
    --band-grey: #9a9ca0;
    --ink: #222222;
  }
  * { margin: 0; padding: 0; box-sizing: border-box; }
  html, body { width: 1200px; height: 900px; overflow: hidden; }
  body {
    background: var(--page);
    display: flex;
    flex-direction: column;
    align-items: center;
    justify-content: center;
    gap: 50px;
    font-family: "Cormorant Garamond", Georgia, serif;
  }
  .card {
    width: 640px;
    height: 366px;
    box-shadow: 0 6px 18px rgba(0,0,0,0.18);
    overflow: hidden;
    position: relative;
  }

  /* Front */
  .card-front {
    background: radial-gradient(ellipse at 30% 20%, var(--card-charcoal) 0%, var(--card-black) 65%);
    color: var(--white);
    padding: 0 52px;
    display: flex;
    flex-direction: column;
    justify-content: flex-end;
    padding-bottom: 70px;
  }
  .brand {
    display: flex;
    align-items: center;
    gap: 16px;
  }
  .brand-square {
    width: 26px; height: 26px;
    background: var(--cream);
  }
  .brand-name {
    font-family: "Cinzel", "Times New Roman", serif;
    font-weight: 400;
    font-size: 38px;
    letter-spacing: 1px;
    color: var(--white);
  }
  .tagline {
    margin-top: 10px;
    margin-left: 42px;
    font-family: "Cinzel", "Times New Roman", serif;
    font-size: 22px;
    letter-spacing: 2px;
    color: var(--cream);
  }

  /* Back */
  .card-back {
    background: var(--paper);
    display: flex;
    flex-direction: column;
  }
  .back-header {
    background: linear-gradient(180deg, #3a3a3a 0%, var(--card-black) 100%);
    color: var(--white);
    height: 104px;
    display: flex;
    flex-direction: column;
    align-items: center;
    justify-content: center;
    padding-left: 160px;
  }
  .person-name { font-size: 30px; font-weight: 500; letter-spacing: 0.5px; }
  .person-title { font-size: 16px; color: #cfcfcf; letter-spacing: 0.5px; }
  .services {
    background: var(--card-black);
    color: var(--white);
    display: flex;
    justify-content: space-between;
    padding: 5px 24px 7px;
    font-size: 14px;
    border-top: 1px solid #555;
  }
  .contact {
    flex: 1;
    padding: 22px 0 0 150px;
    color: var(--ink);
    font-size: 19px;
    line-height: 1.45;
    list-style: none;
  }
  .website {
    background: var(--band-grey);
    color: var(--white);
    text-align: center;
    font-size: 17px;
    letter-spacing: 0.5px;
    padding: 8px 0 10px;
  }
</style>
</head>
<body>
  <section class="card card-back" aria-label="Business card back">
    <header class="back-header">
      <h1 class="person-name">Daniel Hartwell</h1>
      <p class="person-title">Licensed Strata Manager</p>
    </header>
    <nav class="services">
      <span>Strata Management</span>
      <span>Community Management</span>
      <span>Property Management</span>
    </nav>
    <ul class="contact">
      <li>PO Box 48, Millbrook NSW 2088</li>
      <li>16 Carrow Lane Millbrook NSW 2088</li>
      <li>T: 02 9000 1234 &nbsp;F: 02 9000 5678 &nbsp;M: 0400 555 012</li>
      <li>E: info@hartwellproperty.example</li>
    </ul>
    <footer class="website">www.hartwellproperty.example</footer>
  </section>

  <section class="card card-front" aria-label="Business card front">
    <div class="brand">
      <span class="brand-square"></span>
      <span class="brand-name">HARTWELL PROPERTY GROUP</span>
    </div>
    <p class="tagline">STRATA MANAGEMENT SERVICES</p>
  </section>
</body>
</html>
```